Bref créative
Business Cards, Letterhead, Envelopes, Fax Cover, Email Signature, Truck
Brindle Roofing Ltd.
I need double sided standard sized Business Card [3.5" x 2"]
Do not limit yourself to font used in logo
Professional
Tomasz Oduya
42 Fairwick Lane NE
Calgary AB T3M2R8
tomi@brindleroofing.example
www.brindleroofing.example
Open to different ideas. For example : just logo, web address etc
Photograph-1 of truck
Picture 2
Picture-3
Picture-4
Picture-5
Color scheme(s)to be used for Truck

```html
<!DOCTYPE html>
<html lang="en">
<head>
<meta charset="UTF-8">
<title>Brindle Roofing Ltd. — Business Card</title>
<link href="https://fonts.googleapis.com/css2?family=Arimo:wght@400;700&family=Open+Sans:wght@400;600&display=swap" rel="stylesheet">
<style>
  :root {
    --page: #ffffff;
    --card: #ffffff;
    --card-edge: #d6d6d6;
    --brand-grey: #8a8a8a;
    --brand-green: #7fae3a;
    --band-light: #b7d36a;
    --band-dark: #6f9a2e;
    --text-grey: #8f8f8f;
    --label-green: #6f9a2e;
    --name-green: #78a533;
  }
  * { margin: 0; padding: 0; box-sizing: border-box; }
  html, body {
    width: 1200px; height: 341px; overflow: hidden;
    background: var(--page);
  }
  .sheet { position: relative; width: 1200px; height: 341px; }
  .card {
    position: absolute; top: 0; height: 341px;
    background: var(--card);
    border: 1px solid var(--card-edge);
    overflow: hidden;
    font-family: "Arimo", Arial, sans-serif;
  }
  .card--front { left: 0; width: 590px; }
  .card--back { left: 608px; width: 592px; }

  .brand {
    position: absolute; left: 18px; top: 20px;
    display: flex; align-items: center; gap: 12px;
  }
  .brand__dot {
    width: 40px; height: 40px; border-radius: 50%;
    background: var(--brand-green);
  }
  .brand__name {
    font-family: "Open Sans", Arial, sans-serif;
    font-weight: 600; font-size: 40px; letter-spacing: -0.5px;
    color: var(--brand-grey); line-height: 1;
  }

  .address {
    position: absolute; left: 22px; top: 172px;
    font-size: 13px; line-height: 17px; color: var(--text-grey);
  }
  .contact {
    position: absolute; left: 22px; top: 222px;
    font-size: 13px; line-height: 17px; color: var(--text-grey);
  }
  .contact dt { display: inline; font-weight: 700; color: var(--label-green); }
  .contact dd { display: inline; margin: 0; }
  .contact .row { display: block; }
  .email { position: absolute; left: 22px; top: 288px; font-size: 13px; color: var(--text-grey); }
  .email b { color: var(--label-green); }

  .person {
    position: absolute; left: 302px; top: 222px;
    font-size: 18px; font-weight: 700; color: var(--name-green);
  }

  .web-band {
    position: absolute; left: 0; right: 0; bottom: 0; height: 26px;
    background: linear-gradient(90deg, var(--band-dark) 0%, var(--band-light) 55%, var(--band-dark) 100%);
    display: flex; align-items: center; padding-left: 20px;
    font-size: 11px; color: #ffffff;
  }
</style>
</head>
<body>
<div class="sheet">
  <section class="card card--front">
    <div class="brand">
      <span class="brand__dot"></span>
      <span class="brand__name">Brindle Roofing Ltd.</span>
    </div>
    <p class="address">42 Fairwick Lane NE<br>Calgary AB T3M2R8</p>
    <dl class="contact">
      <span class="row"><dt>Phone :</dt> <dd>4035550100</dd></span>
      <span class="row"><dt>Cell :</dt> <dd>4035550100</dd></span>
      <span class="row"><dt>Fax :</dt> <dd>4035550100</dd></span>
    </dl>
    <p class="email"><b>Email :</b> tomi@brindleroofing.example</p>
    <p class="person">Tomasz Oduya</p>
    <div class="web-band">www.brindleroofing.example</div>
  </section>

  <section class="card card--back">
    <div class="brand">
      <span class="brand__dot"></span>
      <span class="brand__name">Brindle Roofing Ltd.</span>
    </div>
    <div class="web-band">www.brindleroofing.example</div>
  </section>
</div>
</body>
</html>
```